Professional and creative business card design for recruiting service providers

Our company supports German medium-sized companies in filling vacancies promptly. For this we use social media marketing and bring our customers into the visibility.

We want a professional but also creative design for our business cards.

Please look at halvenrick-consult.de to get an impression of our CI.

Target Market(s)

Small and medium-sized companies in Germany from the industry

Industry/Entity Type

Industrie, Handwerk

Contact Information for Business Card

Name, Position, Telefonnummer, Email, Website

Colors
EE7325
F08F49
F5BC92
FAE3D3
FDF4ED

Requirements
Must have
• A picture of the employee and in the style of www.halvenrick-consult.de

```html
<!DOCTYPE html>
<html lang="de">
<head>
<meta charset="utf-8">
<title>Halvenrick Consult – Visitenkarte</title>
<link href="https://fonts.googleapis.com/css2?family=Open+Sans:wght@400;700&display=swap" rel="stylesheet">
<style>
  :root{
    --bg:#dcdde0;
    --brand-orange:#f15a2b;
    --card-black:#000000;
    --panel-dark:#0c0808;
    --white:#ffffff;
    --photo-tone-a:#cfc9c2;
    --photo-tone-b:#3a3b40;
  }
  *{margin:0;padding:0;box-sizing:border-box}
  html,body{width:1200px;height:1000px;overflow:hidden}
  body{background:var(--bg);font-family:"Open Sans",Arial,sans-serif;color:var(--white);position:relative}
  .card{position:absolute;left:294px;width:613px;height:352px;border-radius:26px;overflow:hidden}
  .card-front{top:82px;background:var(--brand-orange)}
  .card-back{top:523px;background:var(--card-black)}

  .wordmark{position:absolute;display:flex;align-items:center;font-weight:700;color:var(--white);text-transform:uppercase;line-height:1.1}
  .wordmark .mark-square{background:var(--white);flex:none}
  .card-front .wordmark{left:352px;top:214px;font-size:19px;letter-spacing:.5px;gap:14px}
  .card-front .mark-square{width:40px;height:40px}
  .card-back .wordmark{left:58px;top:66px;font-size:15px;letter-spacing:.4px;gap:12px}
  .card-back .mark-square{width:32px;height:32px;background:var(--brand-orange)}

  .accent-rule{position:absolute;left:58px;top:168px;width:171px;height:3px;background:var(--brand-orange)}
  .contact-panel{position:absolute;left:21px;top:175px;width:268px;height:171px;background:var(--panel-dark)}
  .contact-item{position:absolute;left:37px;display:flex;gap:16px;font-size:14px;line-height:16px}
  .contact-item svg{flex:none;width:16px;height:16px;margin-left:-7px}
  .item-address{top:24px}
  .item-email{top:92px}
  .item-phone{top:127px}

  .portrait{position:absolute;left:393px;top:63px;width:157px;height:157px;border-radius:50%;border:4px solid var(--brand-orange);
    background:linear-gradient(160deg,var(--photo-tone-a) 0%,var(--photo-tone-a) 40%,var(--photo-tone-b) 100%)}
  .person{position:absolute;left:321px;width:300px;text-align:center}
  .person-name{top:240px;font-size:24px;font-weight:700;color:var(--brand-orange)}
  .person-role{top:271px;font-size:14px}
</style>
</head>
<body>
  <section class="card card-front">
    <div class="wordmark"><span class="mark-square"></span><span>Halvenrick<br>Consult</span></div>
  </section>

  <section class="card card-back">
    <div class="wordmark"><span class="mark-square"></span><span>Halvenrick<br>Consult</span></div>
    <div class="accent-rule"></div>
    <div class="contact-panel">
      <div class="contact-item item-address">
        <svg viewBox="0 0 16 16" fill="none" stroke="#fff" stroke-width="1.2"><path d="M8 15s5-5 5-8.5A5 5 0 0 0 3 6.5C3 10 8 15 8 15z"/><circle cx="8" cy="6.5" r="1.8"/></svg>
        <span>Halvenrick Consult GmbH<br>Lindenhofer Strasse 42b<br>70182 Estugarda</span>
      </div>
      <div class="contact-item item-email">
        <svg viewBox="0 0 16 16" fill="none" stroke="#fff" stroke-width="1.2"><rect x="1" y="3.5" width="14" height="9.5"/><path d="M1 3.5l7 6 7-6"/></svg>
        <span>info@halvenrick-consult.de</span>
      </div>
      <div class="contact-item item-phone">
        <svg viewBox="0 0 16 16" fill="#fff"><path d="M4.2 1.5l2 2.6-1.2 1.6c.8 1.9 2.4 3.5 4.3 4.3l1.6-1.2 2.6 2-1.2 2.4C7.400 13 3 8.600 1.8 3.700z"/></svg>
        <span>0171 430 2958</span>
      </div>
    </div>
    <div class="portrait" role="img" aria-label="Porträtfoto des Mitarbeiters im Büro"></div>
    <p class="person person-name">Jan Kessler</p>
    <p class="person person-role">Senior Recruiting Berater</p>
  </section>
</body>
</html>
```